Creative designer wanted for unique pet treats product packaging!

My company is "Barkwell Crisp!" and we're a new and upcoming premium pet treat company. We are different than the rest as we have core values that really stand out and that we're VERY passionate about. They are the following:
HEALTHY-All of our ingredients are fresh and wholesome for dogs. Each has unique health benefits for dogs and there is never any filler-just the good stuff.
AMOUNT OF INGREDIENTS-Most of dog treats have large lists of ingredients and often many of those are difficult to pronounce or people have to look up what they even are. Often there is lot of "filler". We pride ourselves on just having a few ingredients or less. Every ingredient can easily be pronounced, recognized and are commonly consumed by humans in regular meals.
GIVING BACK- We donate a portion of the proceeds of every bag to go to hand selected, accredited and legit animals charities and rescues.
ENVIRONMENT- We strongly care about the environment which is why our bags are compostable. Just simply remove the zipper and track then put the bag in a composting bin. Easy as that. (We have attached a "how to compost your bag in 2 simple steps" image that we would like shown on the bags.
Our initial product is Cinnamon Basil Apple Bark-ley Bites. The ingredients are: Coconut oil, dill, and sweet potato.
We want a design that embodies our values. As well, we have attached "our story" that describes the company and what we are about to consumers. We would like to have it put on the package, but if it cannot be done, then just the meat and potatoes of the message.
A good example for recognition is the attached cake mix as it's simple, portrays the product nicely and when seen from afar-it is easily identified.
*We would like to have a window on the bag that is similar to our paw and leaf logo.
We would also like to see the color green on the package.
Bag specifics are:
Size: 250g OPTIMIZED
Dimensions Inches: 6.15''x9.41''x3.50''
Dimensions mm : 156x239x89
Type: Stand-Up Pouch with Zip (PLOW)
COMPOSTABLE
Material: 100NK MATTE/70NKA/3mil BIOPBS
CMYKW

```html
<!DOCTYPE html>
<html lang="en">
<head>
<meta charset="utf-8">
<title>Barkwell Crisp! – Cinnamon Basil Apple Bark-ley Bites</title>
<link href="https://fonts.googleapis.com/css2?family=Courgette&family=Poppins:wght@600;700&display=swap" rel="stylesheet">
<style>
  :root {
    --bg: #ebebeb;
    --leaf: #8cc63f;
    --leaf-deep: #1fa543;
    --leaf-dark: #14803a;
    --kraft: #b9a98c;
    --kraft-light: #c7b89b;
    --white: #ffffff;
    --brown: #6b4220;
    --oil: #f2b705;
    --potato: #d8671f;
    --dill: #1e8a3c;
    --kibble: #c7862f;
    --kibble-dark: #8a5216;
  }
  * { margin: 0; padding: 0; box-sizing: border-box; }
  html, body { width: 1200px; height: 1000px; overflow: hidden; background: var(--bg); }
  .canvas { position: relative; width: 1200px; height: 1000px; }

  .pouch {
    position: absolute; left: 300px; top: 62px; width: 572px; height: 858px;
    background: var(--kraft);
    background: linear-gradient(180deg, var(--kraft-light), var(--kraft));
    border-radius: 4px 4px 8px 8px;
    overflow: hidden;
  }
  .pouch__top {
    position: absolute; left: 0; top: 0; width: 100%; height: 342px;
    background: var(--leaf);
  }
  .brand-tab {
    position: absolute; left: 240px; top: 0; width: 52px; height: 60px; background: var(--white);
  }
  .brand-seal {
    position: absolute; left: 196px; top: 10px; width: 140px; height: 140px;
    border-radius: 50%; background: var(--white);
    display: flex; align-items: center; justify-content: center; text-align: center;
  }
  .brand-name {
    font-family: 'Poppins', sans-serif; font-weight: 600; font-size: 19px; line-height: 1.15;
    color: var(--brown); width: 110px;
  }
  .product-name {
    position: absolute; left: 0; top: 168px; width: 100%; text-align: center;
    font-family: 'Courgette', cursive; color: var(--white);
    font-size: 50px; line-height: 72px;
    text-shadow: 2px 3px 0 rgba(40, 70, 20, 0.45);
  }
  .tagline {
    position: absolute; left: 0; top: 338px; width: 100%; height: 50px;
    background: var(--leaf-deep);
    display: flex; align-items: center; justify-content: center;
    font-family: 'Poppins', sans-serif; font-weight: 700; font-size: 21px; color: var(--white);
    letter-spacing: 0.2px;
  }
  .window {
    position: absolute; left: 146px; top: 418px; width: 270px; height: 270px;
    border-radius: 50%; border: 4px solid var(--leaf);
    background: radial-gradient(circle at 45% 40%, var(--kibble) 0%, #b5742a 55%, var(--kibble-dark) 100%);
  }
  .ingredient-icons {
    position: absolute; left: 0; top: 708px; width: 100%;
    display: flex; justify-content: center; gap: 22px;
  }
  .ingredient-icons svg { width: 60px; height: 60px; display: block; }
  .ingredients {
    position: absolute; left: 0; top: 795px; width: 100%; text-align: center;
    font-family: 'Poppins', sans-serif; font-weight: 600; font-size: 16.5px; line-height: 26px;
    color: var(--white);
  }
  .pouch__bottom {
    position: absolute; left: 0; bottom: 0; width: 100%; height: 14px; background: var(--leaf);
  }
</style>
</head>
<body>
<main class="canvas">
  <section class="pouch">
    <div class="pouch__top"></div>
    <div class="brand-tab"></div>
    <div class="brand-seal"><span class="brand-name">Barkwell Crisp!</span></div>

    <h1 class="product-name">Cinnamon Basil<br>Apple Bark-ley Bites</h1>
    <div class="tagline">PREMIUM ALL NATURAL DOG TREATS</div>

    <div class="window" role="img" aria-label="Window showing the golden-brown treat bites inside the bag"></div>

    <div class="ingredient-icons">
      <svg viewBox="0 0 60 60" aria-label="Coconut oil">
        <circle cx="30" cy="30" r="30" fill="var(--oil)"/>
        <path d="M30 15 C24 25 21 30 21 35 a9 9 0 0 0 18 0 C39 30 36 25 30 15 Z" fill="var(--white)"/>
      </svg>
      <svg viewBox="0 0 60 60" aria-label="Sweet potato">
        <circle cx="30" cy="30" r="30" fill="var(--potato)"/>
        <ellipse cx="30" cy="30" rx="16" ry="9" transform="rotate(-35 30 30)" fill="none" stroke="var(--white)" stroke-width="2.2"/>
        <path d="M24 34 L36 26" stroke="var(--white)" stroke-width="1.8"/>
      </svg>
      <svg viewBox="0 0 60 60" aria-label="Dill">
        <circle cx="30" cy="30" r="30" fill="var(--dill)"/>
        <g stroke="var(--white)" stroke-width="2" fill="none" stroke-linecap="round">
          <path d="M30 46 L30 18"/>
          <path d="M30 30 L21 21"/><path d="M30 30 L39 21"/>
          <path d="M30 38 L22 31"/><path d="M30 38 L38 31"/>
          <path d="M30 22 L25 15"/><path d="M30 22 L35 15"/>
        </g>
      </svg>
    </div>

    <p class="ingredients">Made with 100% all Natural Ingredients<br>Coconut Oil - Dill - Sweet Potato</p>

    <div class="pouch__bottom"></div>
  </section>
</main>
</body>
</html>
```